Vitalmotion home exercise studio needs a brochure design

My problem is that I have had a fitness studio within my home for 3 years and only 2 clients per week to show for it! I need a fitness brochure designed that will literally want to make a customer pick up the phone and book a training session!

If there is any way possible to convince those exercise lovers or those who wish to become active and healthy who want to train in a private home exercise studio setting than I will be very content and happy. Obviosuly my studio within my home is not exposed to the general public and I understand that this is the reason for a shortage of clients.

I have an exercise studio with my home. It is literally the size of 6-7 x area of a standard bedroom. Most importantly, it contains the latest state of the art exercise equipment (treamills, rowers, cycle & recumberant bikes, elastic cords, bands, medballs, resistance machines, cables, squat racks, you name it..

In addition, compared to many other personal trainers out within the industry, I have clearly distinguished myself from the rest in a positive way. Firstly, I have had an extensive background as an elite athlete (NSW rowing representitive), secondly I have acquired a solid foundation of exercise science principles through 4 years of university studies (compared to most other trainers out there). Because my studio is private and obviously lacks many elements that a typical gym setting such as peak pulse, then we must be able to highlight the positives that arise from my studio compared to peak pulse or any other franchise (eg: no cancellation pollicies, no signing up for contracts, no membership fees). in addition, we must hihglight the fact that a private studio like mine will attract those who prefer not to train around others they do not know as there is no sharing of exercise equipment or duration of time one must be on a certain exercise.

We all know someone who prefers not to train in a typical gym setting where people have to compete against others for the equipment yet alone deal with the amount of starring and chatter that goes on. In addition it can get intimidating for those who prefer not many people around them. My studio is designed for any age or fitness category. In addition group training is avaliable.
In addition, I am flexible and sometimes permit going overtime for those clients who were late for there appointment. Clients that come to my home to exercise feel as if they are training within there own home rather than feeling the intimidation of going into a gym setting such as peak pulse.

If we can highlight all that has been mentioned within my brochure than thats great!

Target Market(s)

I design exercise programs and train all age groups and fitness levels

Industry/Entity Type

University

Requirements
Must have
• There must be a quote in the brochure that mentions "Together,the sky is our limit"

Must have "vitalmotion" logo

must have testimonials:

Owen -"My golf drive has increased dramatically from the use of sports specific exercises that Lachlan was able to deliver. The pain in my lower back has now ceased to flare up after a game"

Marisa - "Lachlan's knowledge and application of exercise science and health has helped me achieve a stronger and leaner body in addition to improving my 5km walking time"

Must have my qualifications:
Certificate 4 personal trainer
Diploma of fitness
Bachelor of exercise and sport science
Diploma of remedial massage
First Aid certificate

Must state that I am registered with Movement Guild

Must have that I Specialize in:

1. exercise rehabilitation
2. sport specific conditioning
3. Functional strength
4. Fat loss and toning
5. Core strength & stability
6. Flexibility
7. Cardio-respiratory fitness

Must have my mobile number: 0498 527 031
Must have my email adress: lchvorenti@mailpost-example.com.au
Nice to have
• any background images that represent motivation, will and determination.

```html
<!DOCTYPE html>
<html lang="en">
<head>
<meta charset="utf-8">
<title>Vitalmotion Brochure</title>
<link href="https://fonts.googleapis.com/css2?family=Gochi+Hand&family=Noto+Sans:ital,wght@0,400;1,400&family=PT+Sans:wght@700&family=Libre+Baskerville:wght@700&display=swap" rel="stylesheet">
<style>
:root{
  --orange:#ef7206;
  --charcoal:#4d4b49;
  --light-grey:#a9a9a9;
  --tan:#e9b48c;
  --white:#ffffff;
  --ink:#141414;
  --brand:#7a1420;
}
*{margin:0;padding:0;box-sizing:border-box}
html,body{width:1200px;height:927px;overflow:hidden;background:var(--white)}
.brochure{position:relative;width:1200px;height:927px;background:var(--white)}
.panel{position:absolute;overflow:hidden}
.panel svg{position:absolute;left:0;top:0}
.photo{position:absolute}

/* testimonials column */
.testimonials{left:12px;top:12px;width:388px;height:903px}
.testimonials .photo{left:0;top:480px;width:388px;height:423px;
  background:linear-gradient(90deg,#c99a7f 0%,#e2bba4 35%,#f4f4f4 62%,#9b9b9b 80%,#d2a184 100%)}
.testimonials h2{position:absolute;left:40px;top:14px;font-family:"Gochi Hand",cursive;font-weight:400;
  font-size:50px;color:var(--white);letter-spacing:1px}
.quote{position:absolute;left:18px;width:358px;font-family:"Noto Sans",sans-serif;font-style:italic;
  font-size:16.5px;line-height:22.6px;color:var(--ink);letter-spacing:.35px;white-space:nowrap}
.quote cite{display:block;text-align:right;font-style:normal;font-size:16.5px;margin-top:2px}
.quote-owen{top:96px}
.quote-marisa{top:258px}

/* studio intro panel */
.studio-intro{left:412px;top:12px;width:773px;height:503px}
.studio-intro .photo{left:0;top:0;width:773px;height:503px;
  background:linear-gradient(160deg,#b7c0c4 0%,#8a8f96 35%,#4f5560 60%,#3f64a8 85%,#2b4f9a 100%)}
.intro-text{position:absolute;left:16px;top:30px;font-family:"Noto Sans",sans-serif;font-style:italic;
  font-size:16.5px;line-height:22.6px;color:var(--ink);letter-spacing:.3px;white-space:nowrap}
.intro-text p{margin-bottom:22px}

/* qualifications */
.qualifications{left:412px;top:530px;width:377px;height:300px;background:var(--charcoal)}
.qualifications h3{margin-top:30px;text-align:center;font-family:"Libre Baskerville",serif;font-weight:700;
  font-variant:small-caps;color:var(--tan);font-size:28px;line-height:31px;letter-spacing:.3px}
.qualifications h3 span{display:block;font-size:25px}
.qual-list{list-style:none;margin:28px 0 0 24px}
.qual-list li{font-family:"PT Sans",sans-serif;font-weight:700;color:var(--white);font-size:17.5px;
  line-height:30.5px;padding-left:16px;position:relative}
.qual-list li::before{content:"";position:absolute;left:0;top:12px;width:7px;height:7px;border-radius:50%;
  background:var(--orange)}

.brand-strip{left:412px;top:836px;width:377px;height:79px;background:var(--light-grey);
  border-radius:0 0 8px 8px;display:flex;align-items:center;justify-content:center;gap:8px}
.brand-mark{width:14px;height:14px;border-radius:50%;background:var(--brand)}
.brand-name{font-family:"PT Sans",sans-serif;font-weight:700;font-size:20px;color:var(--brand)}

/* studio details */
.studio-details{left:801px;top:530px;width:384px;height:385px;background:var(--charcoal)}
.details-text{position:absolute;left:58px;top:8px;font-family:"Noto Sans",sans-serif;
  font-size:14.2px;line-height:21.5px;color:var(--white);white-space:nowrap}
.studio-details .fitness-photo{left:0;top:240px;width:240px;height:145px;
  background:linear-gradient(135deg,#f1d7c7 0%,#f5f3ef 45%,#9dc24a 70%,#2d2d2d 100%)}
.studio-details .trainer-photo{left:247px;top:205px;width:137px;height:180px;
  background:linear-gradient(180deg,#f2eee8 0%,#e4d8c8 55%,#d3473f 80%,#cdbfa9 100%)}
</style>
</head>
<body>
<main class="brochure">

  <section class="panel testimonials">
    <div class="photo" role="img" aria-label="Photo of two toned midriffs in workout wear"></div>
    <svg width="388" height="903" viewBox="0 0 388 903" aria-hidden="true">
      <path d="M0 0H388V520C290 560 140 620 0 700Z" fill="var(--orange)"/>
      <path d="M388 520C290 560 140 620 0 700" fill="none" stroke="var(--white)" stroke-width="4"/>
    </svg>
    <h2>Testimonials</h2>
    <blockquote class="quote quote-owen">"My golf drive has increased dramatically<br>from the use of sports specific exercises<br>that Lachlan was able to deliver. The pain<br>in my lower back has now ceased to flare<br>up after a game"<cite>Owen</cite></blockquote>
    <blockquote class="quote quote-marisa">&nbsp;"Lachlan's knowledge and application of<br>exercise science and health has helped<br>me achieve a stronger and leaner body in<br>addition to improving my 5km walking<br>time"<cite>Marisa</cite></blockquote>
  </section>

  <section class="panel studio-intro">
    <div class="photo" role="img" aria-label="Photo of the home studio with exercise balls, weight plates and resistance machines"></div>
    <svg width="773" height="503" viewBox="0 0 773 503" aria-hidden="true">
      <path d="M0 0H690C500 60 300 200 0 495Z" fill="var(--orange)"/>
      <path d="M690 0C500 60 300 200 0 495" fill="none" stroke="var(--white)" stroke-width="5"/>
    </svg>
    <div class="intro-text">
      <p>"Together, the sky is our limit." Train in a<br>private home studio with no contracts, no<br>membership fees and no cancellation<br>policies. No queues for equipment and no<br>staring, just you, your goals and a trainer<br>registered with Movement Guild.</p>
      <p>I specialise in exercise<br>rehabilitation, sport specific<br>conditioning, functional<br>strength, fat loss and toning,<br>core strength &amp; stability,<br>flexibility and cardio-<br>respiratory fitness.<br>Book your session<br>today!</p>
    </div>
  </section>

  <section class="panel qualifications">
    <h3>Qualified Teacher<span>at your Service</span></h3>
    <ul class="qual-list">
      <li>Certificate 4 personal trainer</li>
      <li>Diploma of fitness</li>
      <li>Bachelor of exercise and sport science</li>
      <li>Diploma of remedial massage</li>
      <li>First Aid certificate</li>
    </ul>
  </section>

  <section class="panel brand-strip">
    <span class="brand-mark"></span><span class="brand-name">Vitalmotion</span>
  </section>

  <section class="panel studio-details">
    <p class="details-text">My studio is 6-7 x the area of a<br>standard bedroom, with state of the art<br>treadmills, rowers, bikes, cords, bands,<br>medballs, cables and squat racks.<br>Any age, any fitness level, groups too.<br>Mobile: 0498 527 031<br>lchvorenti@mailpost-<br>example.com.au<br>Call today!</p>
    <div class="photo fitness-photo" role="img" aria-label="Photo of a green apple, dumbbell and measuring tape"></div>
    <svg width="240" height="385" viewBox="0 0 240 385" aria-hidden="true">
      <path d="M0 385V340C60 300 150 260 240 240V230H0Z" fill="var(--charcoal)"/>
      <path d="M0 340C60 300 150 260 240 240" fill="none" stroke="var(--white)" stroke-width="4"/>
    </svg>
    <div class="photo trainer-photo" role="img" aria-label="Photo of the trainer sitting on an exercise ball"></div>
  </section>

</main>
</body>
</html>
```